Plumtree Crate Society - New Website Design

Create a professional website for strawberries of the month club; a subscription box business that will INCLUDE dipped strawberries - some with sprinkles. Check out: http://www.orchardnook.com for examples. Our website URL will be www.PlumtreeCrateSociety.com
Please see wimplesack.com; fudgeguild.com and gruffcase.com for the concept I am after. The business has not been launched yet, I am currently in the pre-launch stage using a specialized landing page website, and so the time scale for developing my professional looking website is up to 1-2 weeks.
The webpage should have a fun feel and should match the style of the company logo at fudgeguild.com or gruffcase.com. The pages to include are 'Home', 'About us' and 'Get Started'
Thank you and good luck!

```html
<!DOCTYPE html>
<html lang="en">
<head>
<meta charset="utf-8">
<title>Plumtree Crate Society</title>
<link href="https://fonts.googleapis.com/css2?family=Montserrat:wght@400;500;600;700&family=Open+Sans:wght@400;600&family=Lobster&display=swap" rel="stylesheet">
<style>
:root{
  --pink:#f0146e;
  --pink-dark:#d40f5f;
  --teal:#3fcfbf;
  --ink:#333333;
  --muted:#8a8a8a;
  --soft:#f4f4f4;
  --line:#e3e3e3;
  --white:#ffffff;
}
*{margin:0;padding:0;box-sizing:border-box}
html,body{width:1200px;height:3096px;overflow:hidden}
body{font-family:'Open Sans',sans-serif;color:var(--ink);background:var(--white);position:relative}

/* header */
.site-header{height:120px;display:flex;align-items:center;justify-content:space-between;padding:0 72px 0 80px}
.brand{font-family:'Montserrat',sans-serif;font-weight:700;font-size:28px;color:var(--pink);letter-spacing:1px}
.main-nav{display:flex;align-items:center;gap:46px;font-family:'Montserrat',sans-serif;font-size:14px;font-weight:600;color:var(--ink)}
.nav-icons{display:flex;gap:14px;margin-left:-10px}
.nav-icon{flex:none;width:44px;height:44px;border:2px solid var(--pink);border-radius:50%;display:flex;align-items:center;justify-content:center}

/* hero */
.hero{height:512px;position:relative;background:linear-gradient(120deg,#6b1a1f 0%,#b8222c 30%,#8c1b22 55%,#4b5a3a 80%,#3d4b30 100%)}
.hero-copy{position:absolute;left:680px;top:200px;width:480px;color:var(--white)}
.hero-title{font-family:'Montserrat',sans-serif;font-size:30px;font-weight:500;letter-spacing:.5px;white-space:nowrap}
.hero-text{font-size:14px;line-height:22px;margin-top:18px;color:#f3e6e6;width:420px}
.btn{display:inline-block;background:var(--pink);color:var(--white);font-family:'Montserrat',sans-serif;font-weight:600;font-size:14px;border-radius:4px;text-align:center}
.hero .btn{margin-top:20px;padding:14px 26px}
.hero-dots{position:absolute;left:560px;bottom:16px;display:flex;gap:10px}
.hero-dots span{flex:none;width:12px;height:12px;border:2px solid var(--white);border-radius:50%}
.hero-dots span.on{background:var(--white)}

/* sections */
.section-title{font-family:'Lobster',cursive;color:var(--pink);font-size:40px;text-align:center;font-weight:400}
.section-sub{font-size:13px;color:var(--muted);text-align:center;margin-top:14px}

.welcome{height:620px;padding-top:72px}
.steps{display:flex;justify-content:center;gap:130px;margin-top:60px}
.step{width:270px;text-align:center}
.step h3{font-family:'Montserrat',sans-serif;font-size:20px;font-weight:600;margin-top:26px}
.step p{font-size:13px;line-height:24px;color:var(--muted);margin-top:18px}
.teal{color:var(--teal)}.pink{color:var(--pink)}

.features{height:428px;background:var(--soft);padding-top:44px;position:relative}
.crate{position:absolute;left:372px;top:140px;width:456px;height:270px;border-radius:6px;background:linear-gradient(180deg,#c92a35 0%,#b5222c 45%,#d8b585 60%,#c9a070 100%)}
.feature-label{position:absolute;font-family:'Montserrat',sans-serif;font-size:11px;font-weight:700;color:var(--pink)}
.connectors{position:absolute;left:0;top:0}

.pricing{height:700px;padding-top:50px;position:relative}
.plans{position:absolute;left:190px;top:190px;width:820px;height:470px;border-top:1px solid var(--line)}
.plan{position:absolute;top:0;width:260px;height:100%;text-align:center}
.plan h4{font-family:'Montserrat',sans-serif;font-size:16px;font-weight:600;margin-top:46px}
.price{width:110px;height:110px;border-radius:50%;margin:18px auto 0;color:var(--white);display:flex;flex-direction:column;align-items:center;justify-content:center}
.price b{font-family:'Montserrat',sans-serif;font-size:28px;font-weight:600}
.price small{font-size:10px;font-weight:600;letter-spacing:1px}
.plan ul{list-style:none;margin-top:26px}
.plan li{font-size:12px;color:var(--muted);line-height:38px}
.plan .btn{padding:10px 24px;margin-top:14px;font-size:12px}
.plan-std{left:0}.plan-ult{left:560px}
.plan-std .price,.plan-ult .price,.plan-std .btn,.plan-ult .btn{background:var(--teal)}
.plan-prem{left:260px;top:-18px;height:500px;border:3px solid var(--pink);border-radius:8px;background:var(--white)}
.plan-prem .price{background:var(--pink)}
.plan-dot{position:absolute;top:-7px;left:50%;width:14px;height:14px;margin-left:-7px;border-radius:50%}

.gallery{height:400px;background:var(--soft);padding-top:30px}
.photos{display:flex;justify-content:center;gap:72px;margin-top:40px}
.photo{flex:none;width:220px;height:220px;border-radius:50%}

.site-footer{height:260px;background:var(--pink);color:var(--white);position:relative}
.map{position:absolute;left:80px;top:46px;width:240px;height:170px;background:linear-gradient(135deg,#e9e4d8,#d6dcc8);border:4px solid var(--white)}
.foot-col{position:absolute;top:44px}
.foot-col h5{font-family:'Montserrat',sans-serif;font-size:16px;font-weight:700;margin-bottom:18px}
.contact-row{display:flex;align-items:center;gap:12px;font-size:12px;line-height:26px}
.foot-col p{font-size:12px;line-height:22px}
.newsletter-form{display:flex;margin-top:22px}
.newsletter-form .field{width:190px;height:30px;background:var(--white);color:var(--muted);font-size:11px;padding:8px 10px}
.newsletter-form .go{height:30px;padding:0 12px;margin-left:12px;border:1px solid var(--white);font-family:'Montserrat',sans-serif;font-size:11px;font-weight:600;line-height:28px}
.socials{display:flex;gap:10px;margin-top:22px}
.socials span{flex:none;width:34px;height:34px;border:2px solid var(--white);border-radius:50%}
.copyright{height:56px;background:var(--pink-dark);color:var(--white);font-size:12px;text-align:center;line-height:56px}
</style>
</head>
<body>

<header class="site-header">
  <div class="brand">PLUMTREE CRATE SOCIETY</div>
  <nav class="main-nav">
    <span>HOME</span><span>ABOUT US</span><span>GET STARTED</span>
    <div class="nav-icons">
      <span class="nav-icon"><svg width="20" height="20" viewBox="0 0 20 20" fill="none" stroke="#f0146e" stroke-width="2"><path d="M1 3h3l2 9h10l2-6H5"/><circle cx="8" cy="16" r="1.5"/><circle cx="15" cy="16" r="1.5"/></svg></span>
      <span class="nav-icon"><svg width="18" height="18" viewBox="0 0 18 18" fill="none" stroke="#f0146e" stroke-width="2"><circle cx="7.5" cy="7.5" r="5.5"/><path d="M12 12l5 5"/></svg></span>
    </div>
  </nav>
</header>

<section class="hero">
  <div role="img" aria-label="Photo of fresh ripe strawberries with leaves and blossoms on wooden boards" style="position:absolute;inset:0"></div>
  <div class="hero-copy">
    <h1 class="hero-title">PLUMTREE CRATE SOCIETY</h1>
    <p class="hero-text">Fresh picked berries delivered to your door each month, hand dipped and sprinkled for every taste and every occasion.</p>
    <span class="btn">READ MORE</span>
  </div>
  <div class="hero-dots"><span class="on"></span><span></span><span></span></div>
</section>

<section class="welcome">
  <h2 class="section-title">Welcome to Our Company</h2>
  <p class="section-sub">Sweet monthly boxes of fresh berries, hand dipped treats and happy surprises sent straight to your door.</p>
  <div class="steps">
    <div class="step">
      <svg width="96" height="110" viewBox="0 0 96 110"><path d="M48 20 C20 14 8 40 14 62 C20 84 38 104 48 106 C58 104 76 84 82 62 C88 40 76 14 48 20Z" fill="none" stroke="#3fcfbf" stroke-width="4"/><path d="M30 14 L48 22 L66 14 M48 22 V4" fill="none" stroke="#3fcfbf" stroke-width="4"/><text x="48" y="70" text-anchor="middle" font-family="Montserrat,sans-serif" font-size="24" fill="#3fcfbf">01</text></svg>
      <h3 class="teal">Discover Deliciousness</h3>
      <p>Choose from fresh, dipped or sprinkled berries picked at their peak and packed with care for you.</p>
    </div>
    <div class="step">
      <svg width="96" height="110" viewBox="0 0 96 110"><path d="M48 20 C20 14 8 40 14 62 C20 84 38 104 48 106 C58 104 76 84 82 62 C88 40 76 14 48 20Z" fill="none" stroke="#f0146e" stroke-width="4"/><path d="M30 14 L48 22 L66 14 M48 22 V4" fill="none" stroke="#f0146e" stroke-width="4"/><text x="48" y="70" text-anchor="middle" font-family="Montserrat,sans-serif" font-size="24" fill="#f0146e">02</text></svg>
      <h3 class="pink">Your Perfect Box</h3>
      <p>Pick a plan that fits your month, skip or pause any time and gift a box to someone sweet.</p>
    </div>
    <div class="step">
      <svg width="96" height="110" viewBox="0 0 96 110"><path d="M48 20 C20 14 8 40 14 62 C20 84 38 104 48 106 C58 104 76 84 82 62 C88 40 76 14 48 20Z" fill="none" stroke="#3fcfbf" stroke-width="4"/><path d="M30 14 L48 22 L66 14 M48 22 V4" fill="none" stroke="#3fcfbf" stroke-width="4"/><text x="48" y="70" text-anchor="middle" font-family="Montserrat,sans-serif" font-size="24" fill="#3fcfbf">03</text></svg>
      <h3 class="teal">Enter Strawberry Heaven</h3>
      <p>Open your box, share the treats and enjoy a little taste of summer in every single bite.</p>
    </div>
  </div>
</section>

<section class="features">
  <h2 class="section-title">Our Features</h2>
  <p class="section-sub">Everything you love about berries, boxed up with a few sweet extras each and every month.</p>
  <div class="crate" role="img" aria-label="Photo of a wooden crate filled with fresh strawberries"></div>
  <svg class="connectors" width="1200" height="428" viewBox="0 0 1200 428" fill="none" stroke="#f0146e" stroke-width="1.5">
    <path d="M190 220 H330 V250 H372"/><circle cx="190" cy="220" r="4" fill="#f0146e"/>
    <path d="M190 330 H330 V300 H372"/><circle cx="190" cy="330" r="4" fill="#f0146e"/>
    <path d="M1010 226 H870 V250 H828"/><circle cx="1010" cy="226" r="4" fill="#f0146e"/>
    <path d="M1010 330 H870 V310 H828"/><circle cx="1010" cy="330" r="4" fill="#f0146e"/>
  </svg>
  <span class="feature-label" style="left:190px;top:196px">FRESH EVERY MONTH</span>
  <span class="feature-label" style="left:190px;top:340px">HAND DIPPED TREATS</span>
  <span class="feature-label" style="left:880px;top:202px">SPRINKLE TOPPINGS</span>
  <span class="feature-label" style="left:880px;top:340px">FREE HOME DELIVERY</span>
</section>

<section class="pricing">
  <h2 class="section-title">Pricing Plan</h2>
  <p class="section-sub">Three simple plans, each one packed fresh and shipped to your door with no hidden fees.</p>
  <div class="plans">
    <div class="plan plan-std">
      <span class="plan-dot" style="background:#3fcfbf"></span>
      <h4>STANDARD PLAN</h4>
      <div class="price"><b>$7.99</b><small>MONTHLY</small></div>
      <ul><li>One pound of fresh berries</li><li>Seasonal recipe card</li><li>Free monthly shipping</li><li>Pause or skip anytime</li></ul>
      <span class="btn">SIGN UP</span>
    </div>
    <div class="plan plan-prem">
      <span class="plan-dot" style="background:#f0146e;top:-9px"></span>
      <h4>PREMIUM PLAN</h4>
      <div class="price"><b>$20.97</b><small>MONTHLY</small></div>
      <ul><li>Dozen dipped strawberries</li><li>Rainbow sprinkle toppings</li><li>Free monthly shipping</li><li>Pause or skip anytime</li></ul>
      <span class="btn">SIGN UP</span>
    </div>
    <div class="plan plan-ult">
      <span class="plan-dot" style="background:#3fcfbf"></span>
      <h4>ULTIMATE PLAN</h4>
      <div class="price"><b>$25.96</b><small>MONTHLY</small></div>
      <ul><li>Fresh and dipped berries</li><li>Bonus seasonal surprise</li><li>Priority free shipping</li><li>Pause or skip anytime</li></ul>
      <span class="btn">SIGN UP</span>
    </div>
  </div>
</section>

<section class="gallery">
  <h2 class="section-title">Photo Gallery</h2>
  <div class="photos">
    <div class="photo" role="img" aria-label="Photo of a bowl of strawberries" style="background:radial-gradient(circle at 40% 40%,#e0343e,#8e141c)"></div>
    <div class="photo" role="img" aria-label="Photo of strawberries on leaves" style="background:radial-gradient(circle at 50% 40%,#c9303a,#4f6a2e)"></div>
    <div class="photo" role="img" aria-label="Photo of a pile of ripe strawberries" style="background:radial-gradient(circle at 50% 50%,#e8454c,#a51a22)"></div>
    <div class="photo" role="img" aria-label="Photo of cut strawberries on a light table" style="background:radial-gradient(circle at 50% 50%,#f3c9cc,#c62c36)"></div>
  </div>
</section>

<footer class="site-footer">
  <div class="map" role="img" aria-label="Street map showing the shop location"></div>
  <div class="foot-col" style="left:360px">
    <h5>CONTACT US</h5>
    <div class="contact-row"><svg width="14" height="14" viewBox="0 0 14 14" fill="#fff"><path d="M3 1l2 3-1.5 1.5a8 8 0 0 0 5 5L10 9l3 2-1 2.5C6 13 1 8 .5 2z"/></svg>(555) 014 2286 (Phone)</div>
    <div class="contact-row"><svg width="14" height="14" viewBox="0 0 14 14" fill="#fff"><rect x="1" y="3" width="12" height="8" rx="1"/></svg>(555) 014 2287 (Fax)</div>
    <div class="contact-row"><svg width="14" height="14" viewBox="0 0 14 14" fill="none" stroke="#fff" stroke-width="1.5"><rect x="1" y="3" width="12" height="8"/><path d="M1 3l6 5 6-5"/></svg>hello@plumtreecratesociety.com</div>
    <div class="contact-row"><svg width="14" height="14" viewBox="0 0 14 14" fill="#fff"><path d="M7 0a5 5 0 0 0-5 5c0 4 5 9 5 9s5-5 5-9a5 5 0 0 0-5-5zm0 7a2 2 0 1 1 0-4 2 2 0 0 1 0 4z"/></svg>48 Lindenfold Row, Maplecroft</div>
  </div>
  <div class="foot-col" style="left:640px;width:260px">
    <h5>NEWSLETTER</h5>
    <p>Join our mailing list to get sweet news, offers and berry updates.</p>
    <div class="newsletter-form"><span class="field">Email address</span><span class="go">SUBSCRIBE</span></div>
  </div>
  <div class="foot-col" style="left:952px;width:220px">
    <h5>FOLLOW US</h5>
    <p>Share your boxes and follow along for fresh berry news.</p>
    <div class="socials"><span></span><span></span><span></span><span></span><span></span></div>
  </div>
</footer>
<div class="copyright">© Copyright 2024 Plumtree Crate Society. All Rights Reserved.</div>

</body>
</html>
```